Children's martial arts flyer for new classes

Need a postcard flyer addressing the attached spec (see file).

Flyer needs to be Postcard Size and be suited in style to the target demographic which is parents of children aged 5-12 years old.

Classes are new.

Postcard must include the logo and a picture. I have included an example pic in the attached file, but feel free to use other suitable pics.

Target Market(s)

Parents with children aged 5-12 years old

Colors

Designer to choose colors to be used in the design.

Requirements
Must have
• clean look.
• professional.

```html
<!DOCTYPE html>
<html lang="en">
<head>
<meta charset="utf-8">
<title>Children's Martial Art Classes</title>
<link rel="stylesheet" href="https://fonts.googleapis.com/css2?family=Bungee&family=Roboto+Condensed:ital,wght@0,400;0,700;1,400&display=swap">
<style>
  :root {
    --orange: #f08a52;
    --mauve: #8e7672;
    --taupe: #b9a59b;
    --paper: #ffffff;
    --photo-light: #f6efe6;
    --photo-warm: #e6d5c3;
    --map-tone: #ebe7df;
  }
  html, body {
    margin: 0;
    padding: 0;
    overflow: hidden;
    background: var(--paper);
  }
  .flyer {
    position: relative;
    width: 800px;
    height: 1200px;
    overflow: hidden;
    background: var(--paper);
    font-family: "Roboto Condensed", sans-serif;
  }
  .hero-photo {
    position: absolute;
    left: 452px;
    top: 240px;
    width: 332px;
    height: 692px;
    border-radius: 160px 160px 40px 40px;
    background: radial-gradient(ellipse at 60% 35%, var(--photo-light) 0%, var(--photo-warm) 70%, rgba(230,213,195,0) 100%);
  }
  .headline {
    margin: 0;
    font-family: "Bungee", sans-serif;
    font-weight: 400;
  }
  .headline span {
    position: absolute;
    left: 52px;
    display: block;
    font-size: 94px;
    line-height: 94px;
    white-space: nowrap;
    transform: scaleY(1.25);
    transform-origin: 0 84px;
  }
  .headline .line-kids { top: 52px; color: var(--orange); }
  .headline .line-art { top: 172px; color: var(--mauve); letter-spacing: 3px; }
  .headline .line-classes { top: 292px; color: var(--mauve); letter-spacing: 7px; }
  .tagline {
    position: absolute;
    left: 52px;
    top: 404px;
    margin: 0;
    font-style: italic;
    font-weight: 400;
    font-size: 50px;
    line-height: 58px;
    color: var(--taupe);
  }
  .schedule {
    position: absolute;
    left: 50px;
    top: 628px;
    margin: 0;
    font-weight: 700;
    font-size: 40px;
    color: var(--mauve);
    letter-spacing: -0.3px;
  }
  .schedule .divider { color: var(--orange); margin: 0 8px; }
  .location-map {
    position: absolute;
    left: 52px;
    top: 694px;
    width: 438px;
    height: 246px;
    border-radius: 22px;
    background: var(--map-tone);
    box-shadow: 0 3px 8px rgba(0,0,0,0.25);
    border: 4px solid var(--paper);
  }
  .booking {
    position: absolute;
    left: 50px;
    top: 998px;
    margin: 0;
    font-weight: 700;
    font-size: 43px;
    line-height: 49px;
    color: var(--mauve);
  }
  .booking .phone { color: var(--orange); }
  .web-link {
    position: absolute;
    left: 50px;
    top: 1110px;
    margin: 0;
    font-size: 36px;
    color: var(--mauve);
  }
  .brand {
    position: absolute;
    left: 588px;
    top: 1030px;
    width: 176px;
    display: flex;
    flex-direction: column;
    align-items: center;
    gap: 10px;
  }
  .brand-dot {
    width: 64px;
    height: 64px;
    border-radius: 50%;
    background: var(--orange);
  }
  .brand-name {
    font-weight: 700;
    font-size: 30px;
    color: var(--orange);
    white-space: nowrap;
  }
</style>
</head>
<body>
<main class="flyer">
  <div class="hero-photo" role="img" aria-label="Photo of a young student in a white martial arts uniform performing a high front kick"></div>

  <h1 class="headline">
    <span class="line-kids">CHILDREN'S</span>
    <span class="line-art">MARTIAL ART</span>
    <span class="line-classes">CLASSES</span>
  </h1>

  <p class="tagline">Fun and exciting<br>yet controlled and<br>disciplined</p>

  <p class="schedule">Tuesdays and Thursdays<span class="divider">|</span>6pm</p>

  <div class="location-map" role="img" aria-label="Street map showing the class location at 12 Willow Road"></div>

  <p class="booking">Call <span class="phone">0400 218 654</span> to book<br>a free trial class</p>

  <p class="web-link">https://www.kickstartdojo.com.au</p>

  <div class="brand">
    <span class="brand-dot"></span>
    <span class="brand-name">Kickstart Dojo</span>
  </div>
</main>
</body>
</html>
```